Property Investment eBook Cover

I am a long established Australian property investment adviser, analyst and consultant who is now in semi-retired mode and have re-branded to reflect a more casual and personal approach to advising my property investor clients. I am writing a 'revised edition' to a book written in partnership with my father 20 years ago and need an eBook Cover for this new edition. The eBook will be uploaded to all the regular Australian providers (Larkfield Reader, Quince Folio, Tavi, Pagemarten)

The 3 key elements in the book cover are:

Title: The Harvest Engine of Land. The word 'Property' should be larger and more prominent. eg "The Wealth Power of" could be 1/3 the size of "Property" - with both justified left

Edition: Sydney 2021. "Sydney 2021" should be the focus and dominant imagery of the eBook cover and more prominent than the Title or Author

Author: Colin Marsh, The Housing Ledger Guide. The word "Author" should not appear. "The Housing Ledger Guide" should appear underneath Colin Marsh and justified to Colin Marsh, therefore a smaller font.

The cover should be simple, but eye-catching. No property images, more of an abstract background, than a background with an image. Our preferred colour palette is more blues/greens. Prefer SerifFonts

Copy of book published 20 years ago attached for reference only

```html
<!DOCTYPE html>
<html lang="en">
<head>
<meta charset="utf-8">
<title>The Harvest Engine of Land — Colin Marsh</title>
<link rel="stylesheet" href="https://fonts.googleapis.com/css2?family=Bodoni+Moda:wght@600;700&family=Roboto+Condensed:wght@600&display=swap">
<style>
  :root {
    --page-bg: #cfdcdd;
    --cover-base: #c6d5db;
    --cover-light: #dbe3e8;
    --frame: #a9c9cf;
    --panel: rgba(222, 229, 234, 0.72);
    --ink: #121212;
    --badge-red: #b51f2a;
    --badge-red-light: #cc2a33;
    --badge-text: #eef0f2;
  }
  * { margin: 0; padding: 0; box-sizing: border-box; }
  html, body {
    width: 1191px;
    height: 1200px;
    overflow: hidden;
    background: var(--page-bg);
  }
  .cover {
    position: absolute;
    left: 210px;
    top: 40px;
    width: 771px;
    height: 1120px;
    background: linear-gradient(160deg, var(--cover-light) 0%, var(--cover-base) 55%, var(--cover-light) 100%);
    overflow: hidden;
  }
  .cover__wash {
    position: absolute;
    inset: 0;
    background:
      radial-gradient(ellipse 140px 420px at 20px 460px, rgba(134,179,187,0.55), transparent 70%),
      radial-gradient(ellipse 200px 520px at 720px 650px, rgba(159,198,204,0.55), transparent 70%),
      radial-gradient(ellipse 260px 180px at 560px 1020px, rgba(134,179,187,0.45), transparent 70%),
      radial-gradient(ellipse 180px 140px at 200px 1000px, rgba(159,198,204,0.35), transparent 70%);
  }
  .edition {
    position: absolute;
    left: 0;
    top: 0;
    width: 340px;
    height: 250px;
    z-index: 2;
  }
  .edition__shape {
    position: absolute;
    inset: 0;
  }
  .edition__text {
    position: absolute;
    left: 18px;
    top: 52px;
    width: 250px;
    transform: rotate(-34deg);
    font-family: "Roboto Condensed", "Arial Narrow", sans-serif;
    font-weight: 600;
    font-size: 58px;
    line-height: 1.02;
    letter-spacing: 3px;
    color: var(--badge-text);
    text-align: center;
  }
  .cover__frame {
    position: absolute;
    left: 133px;
    top: 244px;
    width: 505px;
    height: 690px;
    border: 24px solid var(--frame);
    background: var(--panel);
  }
  .title {
    position: absolute;
    left: 190px;
    right: 150px;
    top: 350px;
    text-align: left;
    font-family: "Bodoni Moda", "Didot", serif;
    font-weight: 700;
    color: var(--ink);
  }
  .title__lead {
    display: block;
    font-size: 52px;
    line-height: 74px;
    letter-spacing: -1px;
  }
  .title__main {
    display: block;
    margin-top: 40px;
    font-size: 120px;
    line-height: 130px;
    letter-spacing: 8px;
    font-weight: 600;
    margin-left: -6px;
  }
  .author {
    position: absolute;
    left: 0;
    right: 0;
    top: 944px;
    text-align: center;
    font-family: "Bodoni Moda", "Didot", serif;
    font-weight: 700;
    color: var(--ink);
  }
  .author__name {
    display: block;
    font-size: 38px;
    line-height: 44px;
  }
  .author__tagline {
    display: block;
    font-size: 21px;
    line-height: 26px;
  }
</style>
</head>
<body>
  <div class="cover">
    <div class="cover__wash" role="img" aria-label="Abstract pale teal watercolour wash background"></div>

    <div class="edition">
      <svg class="edition__shape" viewBox="0 0 340 250" aria-hidden="true">
        <defs>
          <linearGradient id="editionFill" x1="0" y1="0" x2="1" y2="1">
            <stop offset="0" stop-color="var(--badge-red-light)"/>
            <stop offset="1" stop-color="var(--badge-red)"/>
          </linearGradient>
        </defs>
        <ellipse cx="0" cy="0" rx="330" ry="245" fill="url(#editionFill)"/>
      </svg>
      <div class="edition__text">Sydney<br>2021</div>
    </div>

    <div class="cover__frame"></div>

    <h1 class="title">
      <span class="title__lead">The</span>
      <span class="title__lead">Harvest Engine</span>
      <span class="title__lead">of</span>
      <span class="title__main">LAND</span>
    </h1>

    <p class="author">
      <span class="author__name">Colin Marsh</span>
      <span class="author__tagline">The Housing Ledger Guide</span>
    </p>
  </div>
</body>
</html>
```